Logo Design and Business Card Musician

I need a design for a Business Card and a logo for a professional of music industry. His name is Tomas Velarde: composer, arranger and music producer. You can find him in: [login to view URL], although we are now working in some many changes regarding the site environment. The logo can be with the initials T V, T Ve or any other external suggestion. I request (my idea is, but I am so open), three basic colors: black and white (in any combination) and a different colour. Business card will be two faces: the backside with the link to the web and the logo. Tomas Velarde: composer with experience working with artists, tv, theatre… Some adjectives of his personality: direct, energetic, resolute, fresh, his music is a reflect of his personality. No interest in "obvious" symbols like treble clef, a piano… Thank you very much.

Necesito un diseño de una Business Card y el Logo para un profesional del mundo de la música. El nombre es Tomas Velarde: compositor, arreglista y productor musical. Puedes encontrarlo en [login to view URL], aunque estamos en fase de cambio del entorno de la web. Puede tratarse de un logo con las iniciales T V, T Ve o cualquier sugerencia externa. Solicito, en principio, tres colores básicos: negro y blanco (en cualquier combinación) y un color. La Business card será a dos caras: en la trasera irá solo la web y el logo. Tomas Velarde: compositor con experiencia en artistas, televisión, teatro… directo, contundente, enérgico, fresco, su música es reflejo de su personalidad. No estoy muy interesada en símbolos "obvios" como clave de sol, teclas del piano… Muchas gracias.

```html
<!DOCTYPE html>
<html lang="en">
<head>
<meta charset="utf-8">
<title>Tomas Velarde — Business Card</title>
<link rel="stylesheet" href="https://fonts.googleapis.com/css2?family=Marcellus&family=Quicksand:wght@300;400;500&family=Open+Sans:wght@400&display=swap">
<style>
  :root {
    --backdrop: #d4d4d4;
    --card-dark: #1b1b1b;
    --card-light: #ffffff;
    --accent: #1493bb;
    --ink: #222222;
    --ink-soft: #3a3a3a;
    --rule: #1e1e1e;
  }
  * { margin: 0; padding: 0; box-sizing: border-box; }
  html, body {
    width: 1200px;
    height: 1200px;
    overflow: hidden;
    background: var(--backdrop);
  }
  .canvas {
    position: relative;
    width: 1200px;
    height: 1200px;
  }
  .card {
    position: absolute;
    width: 821px;
    height: 469px;
    border-radius: 18px;
    overflow: hidden;
  }
  .card--back {
    left: 56px;
    top: 107px;
    background: var(--card-dark);
  }
  .card--front {
    left: 315px;
    top: 640px;
    background: var(--card-light);
  }
  .wordmark {
    position: absolute;
    font-family: "Marcellus", Georgia, serif;
    font-weight: 400;
    color: var(--accent);
    text-align: center;
    line-height: 1.15;
  }
  .card--back .wordmark {
    left: 250px;
    top: 150px;
    width: 380px;
    font-size: 54px;
  }
  .card--front .wordmark {
    left: 20px;
    top: 165px;
    width: 380px;
    font-size: 50px;
  }
  .divider {
    position: absolute;
    left: 436px;
    top: 117px;
    width: 3px;
    height: 232px;
    background: var(--rule);
  }
  .holder-name {
    position: absolute;
    left: 496px;
    top: 62px;
    width: 264px;
    text-align: center;
    font-family: "Quicksand", Arial, sans-serif;
    font-size: 32px;
    color: var(--ink);
    letter-spacing: 0.5px;
    line-height: 1;
    padding-bottom: 10px;
    border-bottom: 2px solid var(--rule);
  }
  .holder-name .first { font-weight: 500; }
  .holder-name .last { font-weight: 300; }
  .tagline {
    position: absolute;
    left: 470px;
    top: 127px;
    width: 310px;
    text-align: center;
    font-family: "Quicksand", Arial, sans-serif;
    font-weight: 400;
    font-size: 20px;
    line-height: 28px;
    color: var(--ink-soft);
  }
  .contacts {
    position: absolute;
    left: 480px;
    top: 220px;
    list-style: none;
    font-family: "Open Sans", Arial, sans-serif;
    font-size: 17px;
    color: var(--ink);
  }
  .contact {
    position: absolute;
    left: 0;
    display: flex;
    align-items: flex-start;
    width: 320px;
  }
  .contact svg {
    flex: none;
    width: 22px;
    height: 30px;
    margin-right: 8px;
  }
  .contact span { line-height: 24px; padding-top: 3px; }
  .contact--phone { top: 0; }
  .contact--mail { top: 50px; }
  .contact--web { top: 93px; }
  .contact--address { top: 142px; }
</style>
</head>
<body>
<main class="canvas">

  <section class="card card--back" aria-label="Card back">
    <div class="wordmark">Tomas<br>Velarde</div>
  </section>

  <section class="card card--front" aria-label="Card front">
    <div class="wordmark">Tomas<br>Velarde</div>

    <div class="divider"></div>

    <h1 class="holder-name"><span class="first">Tomas</span> <span class="last">Velarde</span></h1>

    <p class="tagline">composer with experience<br>working with artists, tv, theatre</p>

    <ul class="contacts">
      <li class="contact contact--phone">
        <svg viewBox="0 0 22 30" aria-hidden="true">
          <rect x="4" y="2" width="14" height="26" rx="2.5" fill="none" stroke="#222" stroke-width="2"/>
          <line x1="4" y1="6.5" x2="18" y2="6.5" stroke="#222" stroke-width="1.5"/>
          <line x1="4" y1="23" x2="18" y2="23" stroke="#222" stroke-width="1.5"/>
          <circle cx="11" cy="25.5" r="1" fill="#222"/>
        </svg>
        <span>+91-5550147286</span>
      </li>
      <li class="contact contact--mail">
        <svg viewBox="0 0 22 30" aria-hidden="true">
          <rect x="2" y="8" width="15" height="16" fill="none" stroke="#222" stroke-width="2"/>
          <path d="M8 19 L9 15 L18 6 L21 9 L12 18 Z" fill="#222"/>
        </svg>
        <span>info@tomasvelardemusic.com</span>
      </li>
      <li class="contact contact--web">
        <svg viewBox="0 0 22 30" aria-hidden="true">
          <rect x="5" y="7" width="12" height="19" rx="6" fill="none" stroke="#222" stroke-width="2"/>
          <line x1="11" y1="8" x2="11" y2="13" stroke="#222" stroke-width="2"/>
          <path d="M11 7 C11 3 6 4 6 1" fill="none" stroke="#222" stroke-width="1.5"/>
        </svg>
        <span>www.tomasvelardemusic.com</span>
      </li>
      <li class="contact contact--address">
        <svg viewBox="0 0 22 30" aria-hidden="true">
          <circle cx="11" cy="8" r="5" fill="#222"/>
          <line x1="11" y1="12" x2="11" y2="25" stroke="#222" stroke-width="2"/>
          <ellipse cx="11" cy="26" rx="4" ry="1.6" fill="none" stroke="#222" stroke-width="1.5"/>
        </svg>
        <span>Sample text for Address,<br>city</span>
      </li>
    </ul>
  </section>

</main>
</body>
</html>
```